Need a landing page design.

We are currently trying to develop a landing page for our www.brightoakwellness.example website.

Objective: To peak a level of interest in Medical Practices to sign up to our program and promote our line of vitamins and supplements. We will be concentrating on email marketing as well as fax or direct mail to drive medical facilities to our landing page.

Page requirements:
1. A slider on the top portion showing our line of products from the brightoakwellness.example website.
2. An "about us" area to explain who we are and what we offer.
3. An area for a grid so that we can show potential earnings for the practice as part of our program.
4. A Testimonial area for a couple of testimonials
5. A scroll area where they can see our contract
6. A lead capture area where they can input their contact information so we may gather it and contact them back to explain the program. In this area I need the following fields: Name of Practice; Contact name; Email address; Phone Number; Area of Medical Discipline; Number of patients per day.
7. A nice clean contact us area

Other than these main requirements the rest is up to you.

Goal: Entice Medical practices to use our FREE service to increase revenue for their offices while helping their patients save money on their supplements.

Key Factors for the Medical facility to know: Free to sign up, no inventory carrying costs. Simple backend sales area to process orders. We handle all shipping and customer service.

Thank you

Target Market(s)

Medical Facilities, mainly office managers and docotors

Industry/Entity Type

Marketing

Requirements
Must have
• Professional design as we are dealing with the medical field.

```html
<!DOCTYPE html>
<html lang="en">
<head>
<meta charset="utf-8">
<title>Bright Oak Wellness – Practice Program</title>
<link href="https://fonts.googleapis.com/css2?family=Mulish:wght@400;600;700;800&family=Open+Sans:ital,wght@0,400;0,700;1,700&display=swap" rel="stylesheet">
<style>
:root{
  --ink:#222;
  --brown:#6b4b2a;
  --brown-dark:#4a2e12;
  --red:#e0282e;
  --teal:#8fd3d6;
  --teal-pale:#b2e0e3;
  --nav-top:#c98624;
  --nav-bot:#7a4a12;
  --green:#2f7d12;
  --grey-bar:#cfcfcf;
  --dark:#262626;
  --footer-text:#d8d8d8;
}
*{margin:0;padding:0;box-sizing:border-box}
html,body{width:853px;height:1200px;overflow:hidden;background:#fff}
body{position:relative;font-family:"Open Sans",sans-serif;color:var(--ink)}
.abs{position:absolute}
.topbar{left:0;top:0;width:853px;height:22px;background:var(--ink);color:#fff;font:700 10px "Mulish",sans-serif;text-align:right;padding:5px 105px 0 0;letter-spacing:.3px}
.brand{left:96px;top:56px;display:flex;align-items:center;gap:8px}
.brand-mark{width:22px;height:22px;border-radius:50%;background:var(--teal)}
.brand-name{font:800 15px "Mulish",sans-serif;color:var(--brown)}
.cart{left:642px;top:62px;display:flex;align-items:center;gap:6px;font:800 9.5px "Mulish",sans-serif}
.phone{right:103px;top:90px;font:800 21px "Mulish",sans-serif;color:var(--brown)}
.hero{left:0;top:123px;width:853px;height:269px;background:linear-gradient(90deg,#bfe6e7 0%,#e9f6f6 35%,#d8d0c4 55%,#c9b49c 70%,#9fd3d4 100%)}
.hero-photo{left:360px;top:123px;width:400px;height:269px;background:linear-gradient(180deg,rgba(214,196,172,.6),rgba(182,150,118,.55))}
.hero-title{left:78px;top:216px;width:248px;font:800 23px/28px "Mulish",sans-serif;color:var(--red);text-align:center;white-space:nowrap}
.btn-signup{left:151px;top:294px;width:96px;height:29px;background:var(--red);color:#fff;font:800 16px/29px "Mulish",sans-serif;text-align:center}
.pager{left:127px;top:360px;display:flex;gap:7px}
.pager span{width:19px;height:19px;background:#111;color:#fff;font:700 14px/19px "Mulish",sans-serif;text-align:center}
.pager span.on{background:var(--brown)}
.nav{left:0;top:392px;width:853px;height:40px;background:linear-gradient(180deg,var(--nav-top),var(--nav-bot))}
.nav-item{top:403px;height:20px;font:600 9.5px/20px "Mulish",sans-serif;color:#fff;text-align:center;white-space:nowrap}
.nav-home{left:118px;width:49px;background:#fff;color:var(--brown);border-radius:2px}
.search-input{left:626px;top:406px;width:84px;height:13px;background:#fff;border-radius:2px}
.search-go{left:715px;top:406px;width:22px;height:14px;background:#6fc7d0;color:#fff;font:700 8px/14px "Mulish",sans-serif;text-align:center;border-radius:3px}
.sep{top:398px;width:1px;height:28px;background:rgba(255,255,255,.25)}
h2.section{font:800 20px "Mulish",sans-serif;color:var(--brown);letter-spacing:.3px;white-space:nowrap}
.rule{height:2px;background:var(--brown)}
.welcome-text{left:98px;top:491px;width:372px;font-size:8.6px;line-height:11px;text-align:justify}
.welcome-text p+p{margin-top:11px}
.btn-more{height:17px;background:linear-gradient(180deg,#9b7d62,#5e4532);color:#fff;font:800 8.5px/17px "Mulish",sans-serif;text-align:center;border-radius:2px}
.testimonial{left:534px;top:446px;width:223px;height:239px;border:3px solid #e4e4e4}
.testimonial h2{text-align:center;margin-top:8px}
.testimonial .rule{margin:4px 10px 0}
.quote{margin:10px 0 0 40px;width:150px;font-size:8.6px;line-height:18px}
.quote-by{margin:2px 0 0 0;width:186px;text-align:right;font:italic 700 8.6px "Open Sans",sans-serif}
.earn-panel{left:96px;top:696px;width:378px;height:378px;background:#fff}
.earn-row{left:102px;width:368px;height:98px}
.thumb{position:absolute;left:0;top:0;width:59px;height:49px;border:1px solid #bbb;font:700 8px "Open Sans",sans-serif;color:#fff;text-align:center;padding-top:6px}
.thumb-label{position:absolute;left:0;top:53px;width:59px;text-align:center;font:400 9.5px/10px "Mulish",sans-serif;color:var(--brown)}
.row-text{position:absolute;left:68px;top:0;width:215px;font-size:8.6px;line-height:18px}
.btn-visit{position:absolute;left:288px;top:32px;width:52px;height:17px;background:linear-gradient(180deg,#3f9b1b,#215c0c);color:#fff;font:800 9px/17px "Mulish",sans-serif;text-align:center}
.grey-bar{left:96px;width:374px;height:5px;background:var(--grey-bar)}
.contact-head{left:544px;top:715px;width:201px;height:27px;background:var(--brown-dark);color:#fff;font:800 15px/27px "Mulish",sans-serif;padding-left:26px}
.contact-fold{left:700px;top:713px}
.contact-form{left:558px;top:742px;width:187px;height:260px;background:var(--teal-pale);border-bottom:3px solid #8fb8bb}
.f-label{position:absolute;font:700 7.5px "Open Sans",sans-serif;white-space:nowrap}
.f-input{position:absolute;left:50px;width:124px;height:12px;background:#fff;border:1px solid #9cc}
.btn-submit{position:absolute;left:70px;top:217px;width:86px;height:22px;background:var(--brown-dark);color:#fff;font:800 12px/22px "Mulish",sans-serif;text-align:center}
.footer{left:0;top:1032px;width:853px;height:168px;background:var(--dark)}
.page-lip{left:96px;top:1032px;width:658px;height:42px;background:#fff}
.btn-plus{left:103px;top:1030px;width:64px;height:26px;background:var(--brown-dark);color:#fff;font:800 12px/26px "Mulish",sans-serif;text-align:center;border-radius:2px}
.follow{left:540px;top:1031px;height:20px;display:flex;align-items:center;gap:5px;font:800 14px "Mulish",sans-serif;white-space:nowrap}
.social{font:700 6.5px "Mulish",sans-serif;display:flex;align-items:center;gap:3px}
.social i{width:8px;height:8px;border-radius:50%;background:var(--ink);display:inline-block}
.f-head{font:600 11px "Mulish",sans-serif;color:#fff;letter-spacing:.5px}
.links{left:103px;top:1122px;display:grid;grid-template-columns:78px 110px;row-gap:4px;font:400 8px "Mulish",sans-serif;color:var(--footer-text);white-space:nowrap}
.badge{top:1099px;height:41px}
.cards{left:363px;top:1164px;display:flex;gap:4px}
.cards span{width:25px;height:17px;background:#eee;border-radius:2px}
.accept{left:380px;top:1148px;font:400 9px "Mulish",sans-serif;color:#fff;letter-spacing:.5px}
.contact-info{left:552px;top:1118px;width:200px;font:400 8.5px/10.5px "Open Sans",sans-serif;color:var(--footer-text)}
.copyright{left:0;top:1188px;width:853px;height:12px;background:#111;color:#bbb;font:400 6.5px/12px "Open Sans",sans-serif;text-align:center}
</style>
</head>
<body>

<div class="abs topbar">MY ACCOUNT &nbsp;|&nbsp; LOG IN</div>

<div class="abs brand">
  <span class="brand-mark"></span>
  <span class="brand-name">Bright Oak Wellness</span>
</div>

<div class="abs cart">
  <svg width="24" height="20" viewBox="0 0 24 20"><path d="M1 2h4l3 11h12l3-8H7" fill="none" stroke="#222" stroke-width="2"/><circle cx="10" cy="17" r="2" fill="#222"/><circle cx="18" cy="17" r="2" fill="#222"/></svg>
  SHOPPING CART
</div>
<div class="abs phone">Call: (888) 555-0142</div>

<div class="abs hero"></div>
<div class="abs hero-photo" role="img" aria-label="Photo of two lab researchers in white coats reviewing papers"></div>
<div class="abs hero-title">NOW<br>FREE TO SIGN UP</div>
<div class="abs btn-signup">SIGN UP</div>
<div class="abs pager"><span class="on">1</span><span>2</span><span>3</span><span>4</span><span>5</span></div>

<nav class="abs nav"></nav>
<div class="abs nav-item nav-home">HOME</div>
<div class="abs nav-item" style="left:190px;width:58px">ABOUT US</div>
<div class="abs sep" style="left:264px"></div>
<div class="abs nav-item" style="left:276px;width:62px">PRODUCTS</div>
<div class="abs sep" style="left:350px"></div>
<div class="abs nav-item" style="left:362px;width:100px">ASKED QUESTIONS</div>
<div class="abs sep" style="left:470px"></div>
<div class="abs nav-item" style="left:482px;width:66px">CONTACTS</div>
<div class="abs sep" style="left:565px"></div>
<div class="abs nav-item" style="left:578px;width:44px">SEARCH</div>
<div class="abs search-input"></div>
<div class="abs search-go">GO</div>

<h2 class="abs section" style="left:101px;top:452px">WELCOME TO OUR WEB SITE,</h2>
<div class="abs rule" style="left:96px;top:481px;width:374px"></div>
<div class="abs welcome-text">
  <p>Bright Oak has a strong line of new and innovative health products manufactured in a GMP certified facility right here in the USA. The ingredients in Bright Oak Wellness's products are chosen by medical professionals in the corresponding field of expertise for the utmost quality. Bright Oak Wellness has one main goal: to provide high quality products that make a healthy difference in people's lives.</p>
  <p>Bright Oak Wellness offers an Easy Auto Ship Program. The Easy Auto Ship Program is setup to have your vitamins sent directly to your home or business, based on your desired frequency. Not only do you get on-time shipping for FREE, but you also get a discounted rate. Take advantage of the shipping convenience and discounted rates, with the ability to cancel at ANY time, no hassle, no fees.</p>
</div>
<div class="abs btn-more" style="left:371px;top:651px;width:71px">READ MORE</div>

<section class="abs testimonial">
  <h2 class="section">TESTIMONIAL</h2>
  <div class="rule"></div>
  <p class="quote">“Lorem Ipsum is simply dummy text of the printing and typesetting industry. Lorem Ipsum has been the industry's standard dummy text ever since the 1500s, when an unknown” printer took a galley of &nbsp;Lorem Ipsum</p>
  <p class="quote-by">- DANIEL MARSH</p>
  <div class="btn-more" style="margin:14px 0 0 76px;width:71px">READ MORE</div>
</section>

<div class="abs earn-panel"></div>
<h2 class="abs section" style="left:101px;top:709px">MEDICAL POTENTIAL EARNINGS,</h2>
<div class="abs rule" style="left:96px;top:738px;width:348px"></div>

<div class="abs earn-row" style="top:745px">
  <div class="thumb" style="background:#16395e">$384,467</div>
  <div class="thumb-label">Specialty<br>Care</div>
  <p class="row-text">“Lorem Ipsum is simply dummy text of the printing and typesetting industry. Lorem Ipsum has been the industry's standard dummy text ever since the 1500s, when an unknown” printer</p>
  <div class="btn-visit">VISIT</div>
</div>
<div class="abs grey-bar" style="top:826px"></div>
<div class="abs earn-row" style="top:843px">
  <div class="thumb" style="background:#c8141c">$212,840</div>
  <div class="thumb-label">Primary<br>Care</div>
  <p class="row-text">“Lorem Ipsum is simply dummy text of the printing and typesetting industry. Lorem Ipsum has been the industry's standard dummy text ever since the 1500s, when an unknown” printer</p>
  <div class="btn-visit">VISIT</div>
</div>
<div class="abs grey-bar" style="top:924px"></div>
<div class="abs earn-row" style="top:941px">
  <div class="thumb" style="background:linear-gradient(180deg,#dfe9f3,#2f62a8)" role="img" aria-label="Product photo of supplement bottles"></div>
  <p class="row-text">“Lorem Ipsum is simply dummy text of the printing and typesetting industry. Lorem Ipsum has been the industry's standard dummy text ever since the 1500s, when an unknown” printer</p>
  <div class="btn-visit">VISIT</div>
</div>

<div class="abs contact-head">QUICK CONTACT</div>
<svg class="abs contact-fold" width="46" height="46" viewBox="0 0 46 46"><polygon points="0,2 16,2 46,32 46,46" fill="#f2c400"/></svg>
<form class="abs contact-form">
  <span class="f-label" style="left:14px;top:24px">Name:</span><span class="f-input" style="top:22px"></span>
  <span class="f-label" style="left:14px;top:42px">E-mail:</span><span class="f-input" style="top:40px"></span>
  <span class="f-label" style="left:14px;top:60px">Title:</span><span class="f-input" style="top:58px"></span>
  <span class="f-label" style="left:62px;top:75px">Website URL (if any):</span><span class="f-input" style="top:87px"></span>
  <span class="f-label" style="left:58px;top:102px">Number of patients per day</span><span class="f-input" style="top:114px"></span>
  <span class="f-label" style="left:58px;top:129px">Area of Medical Discipline</span><span class="f-input" style="top:141px"></span>
  <span class="f-label" style="left:14px;top:160px">Role:</span><span class="f-input" style="top:158px"></span>
  <span class="f-label" style="left:14px;top:178px">City:</span><span class="f-input" style="top:176px"></span>
  <span class="f-label" style="left:14px;top:196px">Zip:</span><span class="f-input" style="top:194px"></span>
  <span class="btn-submit">SUBMIT</span>
</form>

<footer class="abs footer"></footer>
<div class="abs page-lip"></div>
<div class="abs btn-plus">+ MORE</div>
<div class="abs follow">FOLLOW US:
  <span class="social"><i></i>Friendly</span>
  <span class="social"><i></i>Chirper</span>
  <span class="social"><i></i>Stackly</span>
</div>

<div class="abs f-head" style="left:103px;top:1102px">QUICK LINKS</div>
<div class="abs links">
  <span>HOME</span><span>PRODUCT</span>
  <span>ABOUT US</span><span>CONTACT US</span>
  <span>ASKED QUESTIONS</span><span>PRIVACY POLICY</span>
  <span>RETURN POLICY</span><span>TERMS AND CONDITIONS</span>
</div>

<svg class="abs badge" style="left:314px" width="46" height="46" viewBox="0 0 46 46"><circle cx="23" cy="23" r="21" fill="#d4a21a"/><circle cx="23" cy="23" r="15" fill="#b5830c"/></svg>
<div class="abs badge" style="left:368px;width:64px;background:#f4f4e8;border:2px solid #8cc63f"></div>
<div class="abs badge" style="left:440px;width:54px;background:#fff;border:2px solid #2b8a3e"></div>
<div class="abs accept">WE ACCEPT</div>
<div class="abs cards"><span style="background:#1a3d8f"></span><span style="background:#e8e8e8"></span><span style="background:#dfe6ee"></span><span style="background:#2a76c9"></span></div>

<div class="abs f-head" style="left:552px;top:1100px">CONTACT INFORMATION</div>
<div class="abs contact-info">Call: 888-555-0142 (9am-5pm EST, Monday–Friday)<br>Email: support@brightoakwellness.example<br>Mail: 410 Harbor Lane Suite #12, Fernview, FL 32000</div>

<div class="abs copyright">Copyright © 2013 Bright Oak Wellness. All Rights Reserved</div>

</body>
</html>
```